Training Course Info Brochure

Hi there, I'm looking for a design for A4 Flyer (2-3 pages) on our new Course - Infection Control. I have included a previous brochure on our courses so the designed can see the look and feel we are looking for.

As this is about Infection Control, I would also like to see some RED in the design or wording.

The brochure will need to include quite a few industry/ government logos as well and graphics are important. I have included some (Health Care Industry workers) and am also open to other graphics.

Thanks for considering!

Target Market(s)

The Health profession and students wanting to work in the health field

Industry/Entity Type

Health Care

Font styles to use
Sans Serif

Colors
3277b5
f78f20
ffffff
ec1f27

Requirements
Must have
• Similar feel to the brochure I have included in this brief.

SOME RED lettering as we are teaching Infection Control during the COVID19 pandemic
Nice to have
• Lovely design with quite a few photos graphics

Company details:

Carrow Academy of Learning
RTO 73648
FREECALL : 1800 437 982
www.carrowlearning.edu.au
info@carrowlearning.edu.au

```html
<!DOCTYPE html>
<html lang="en">
<head>
<meta charset="utf-8">
<title>Infection Control Skill Set Brochure</title>
<link rel="stylesheet" href="https://fonts.googleapis.com/css2?family=Montserrat:wght@400;500;600;700;800&family=Kaushan+Script&display=swap">
<style>
:root{
  --blue:#3277b5;
  --orange:#f78f20;
  --red:#ec1f27;
  --deep-red:#c8161d;
  --white:#ffffff;
  --ink:#3a3a3a;
  --navy:#1e2a4a;
  --gold:#d9a92a;
  --stage:#1f3a3a;
  --panel:#f0f0f2;
}
*{box-sizing:border-box;margin:0;padding:0}
html,body{width:1200px;height:1200px;overflow:hidden}
body{background:var(--stage);font-family:"Montserrat",sans-serif;color:var(--ink);position:relative}
.page{position:absolute;width:400px;height:560px;background:var(--white);overflow:hidden}
.p1{left:190px;top:30px}.p2{left:610px;top:30px}
.p3{left:190px;top:610px}.p4{left:610px;top:610px}
.abs{position:absolute}
.bars{position:absolute;left:4px;right:4px;bottom:6px;height:9px;display:flex;gap:7px}
.bars span{flex:1}
.bars .o{background:var(--orange)}.bars .r{background:var(--deep-red)}.bars .b{background:var(--blue)}

/* cover */
.cover-photo{left:0;top:0;width:400px;height:314px;background:linear-gradient(120deg,#c9d4dc 0%,#eef1f3 45%,#e8dccd 75%,#f4f4f4 100%)}
.brand-mark{left:38px;top:26px;width:90px;font-size:7px;font-weight:700;color:var(--navy);text-align:center;letter-spacing:.5px;line-height:1.3}
.cover-title{left:86px;top:146px;width:225px;height:126px;background:var(--red);color:var(--white);text-align:center;padding-top:10px}
.cover-title .t1{font-size:22px;font-weight:800}
.cover-title .t2{font-size:20px;font-weight:400;margin-top:2px}
.cover-title .t3{font-size:16px;margin-top:2px}.cover-title .t3 b{font-weight:800}
.cover-title .t4{font-size:16px;margin-top:2px}
.unit-band{left:0;top:314px;width:400px;height:72px;background:var(--blue);color:var(--white);text-align:center;font-size:14.5px;line-height:1.35;padding-top:6px}
.cost-box{left:40px;top:413px;width:318px;height:73px;border:1.5px solid var(--deep-red);text-align:center}
.cost-box h3{position:absolute;left:50%;top:-11px;transform:translateX(-50%);background:var(--white);padding:0 8px;color:var(--deep-red);font-size:15.5px;font-weight:800;white-space:nowrap}
.cost-box .l1{color:var(--deep-red);font-size:13px;margin-top:12px}
.cost-box .l2{font-size:17px;color:#333;line-height:1.15}
.cost-box .l3{color:var(--deep-red);font-size:14px;font-weight:800}
.contact{top:510px;font-size:7.2px;font-weight:600;color:#222;line-height:1.3}
.contact.left{left:90px;width:110px;text-align:right}
.contact.right{left:220px}

/* back cover */
.back-photo{left:0;top:0;width:400px;height:284px;background:linear-gradient(160deg,#2f5f9e 0%,#3f7fc4 40%,#2a5590 100%)}
.partners{left:28px;top:302px;width:344px;display:flex;align-items:center;justify-content:space-between;gap:6px}
.partner{display:flex;align-items:center;gap:4px;font-size:7px;font-weight:700;line-height:1.15;color:var(--blue)}
.partner i{display:block;width:14px;height:14px;flex:none}
.rule{left:20px;top:358px;width:360px;height:1px;background:#cfcfcf}
.tagline{left:0;top:380px;width:400px;text-align:center;font-family:"Kaushan Script",cursive;color:var(--gold);font-size:30px;line-height:1.15;transform:rotate(-4deg)}
.back-band{left:0;top:480px;width:400px;height:40px;background:var(--blue);color:var(--white);font-size:8px;font-weight:600;line-height:1.3}
.back-band .a{position:absolute;left:53px;top:11px}.back-band .b{position:absolute;left:226px;top:11px}
.web{left:0;top:532px;width:400px;text-align:center;font-size:8px;font-weight:600;letter-spacing:3.4px;color:var(--blue)}

/* inside left */
.side-photo{left:0;top:0;width:222px;height:420px;background:linear-gradient(180deg,#dfe5ea 0%,#eadfd3 45%,#3b5c8c 100%)}
.side-blue{left:0;top:360px;width:222px;height:190px;background:var(--blue)}
.skills{left:15px;top:178px;width:192px;height:188px;background:rgba(30,38,70,.93);border-radius:8px;padding:8px 10px;color:var(--white)}
.skills h4{color:var(--red);font-size:11.5px;font-weight:600;border-bottom:1px solid #fff;padding-bottom:3px;width:150px}
.skills li{list-style:none;font-size:5.8px;line-height:1.4;padding:3px 0 3px 6px;border-bottom:1px solid rgba(255,255,255,.35);position:relative}
.skills li::before{content:"";position:absolute;left:0;top:5px;width:3px;height:3px;border:1px solid var(--red);border-radius:50%}
.ideal{left:22px;top:370px;width:184px;color:var(--white)}
.ideal h4{font-size:11.5px;font-weight:600;margin-bottom:8px}
.ideal p{font-size:6px;line-height:1.45;text-align:justify;margin-bottom:7px}
.ideal li{list-style:none;font-size:6px;line-height:1.45;padding:3px 0 3px 6px;border-bottom:1px solid rgba(255,255,255,.45);position:relative}
.ideal li::before,.col li::before{content:"";position:absolute;left:0;top:5px;width:3px;height:3px;border:1px solid var(--red);border-radius:50%}
.col{left:232px;top:16px;width:160px}
.col li{list-style:none;font-size:6px;line-height:1.45;padding:4px 0 5px 8px;border-bottom:1px solid #bbb;position:relative}
.col h4{color:var(--orange);font-size:11.5px;font-weight:600;line-height:1.2;margin:14px 0 8px 4px}
.col p{font-size:6px;line-height:1.55;text-align:justify;margin:0 0 8px 4px}
.col .quals li{font-size:5.3px;padding:3px 0 3px 5px}
.col .quals li::before{width:2px;height:2px;border:none;background:var(--blue);top:6px}
.more{left:232px;top:484px;width:160px;text-align:center;color:var(--blue);font-size:10px;line-height:1.2}
.more b{color:var(--deep-red);font-weight:600}
.more small{display:block;font-size:5px;font-weight:600;margin-top:4px}

/* inside right */
.about-head{left:20px;top:12px;width:210px}
.about-head h2{color:var(--deep-red);font-size:15.5px;font-weight:700;background:var(--panel);padding:0 0 2px 2px}
.about-head h5{color:var(--deep-red);font-size:7.5px;font-weight:700;margin-top:10px;line-height:1.3}
.about-photo{left:232px;top:12px;width:153px;height:207px;background:linear-gradient(160deg,#e7ecef 0%,#cfe2e6 50%,#9fd2d6 100%)}
.txt{font-size:6px;line-height:1.6;text-align:justify;color:#444}
.txt p{margin-bottom:8px}.txt .red{color:var(--deep-red);font-weight:700}
.about-a{left:22px;top:72px;width:205px}
.about-b{left:22px;top:235px;width:362px}
.format{left:8px;top:308px;width:382px;height:226px;background:var(--panel);padding:6px 10px}
.format h3{color:var(--deep-red);font-size:9.5px;font-weight:600;margin:3px 0 6px}
.format h3.first{border-bottom:1px solid #999;padding-bottom:3px;margin-left:-10px;padding-left:10px;margin-right:-10px}
.format .txt{font-size:5.8px;line-height:1.5}
.format .txt p{margin-bottom:6px}
</style>
</head>
<body>

<!-- Cover -->
<section class="page p1">
  <div class="abs cover-photo" role="img" aria-label="Photo of a smiling health care worker in a white uniform in a clinical room"></div>
  <div class="abs brand-mark">CARROW ACADEMY<br>OF LEARNING</div>
  <div class="abs cover-title">
    <div class="t1">Infection Control</div>
    <div class="t2">Skill set</div>
    <div class="t3"><b>HLTSS00064</b> for</div>
    <div class="t4">Health Care workers</div>
  </div>
  <div class="abs unit-band"><b>HLTINF001 - Comply with</b><br><b>infection</b> prevention and control<br>policies and procedures</div>
  <div class="abs cost-box">
    <h3>Course cost</h3>
    <div class="l1">Free infection control skill sets for</div>
    <div class="l2">everyone in Western Australia or</div>
    <div class="l3">$350/for students outside of WA.</div>
  </div>
  <div class="abs contact left">Carrow Academy of Learning<br>RTO 73648</div>
  <div class="abs contact right">FREECALL : 1800 437 982<br>info@carrowlearning.edu.au<br>www.carrowlearning.edu.au</div>
  <div class="bars"><span class="o"></span><span class="r"></span><span class="b"></span></div>
</section>

<!-- Back cover -->
<section class="page p2">
  <div class="abs back-photo" role="img" aria-label="Photo of a health worker in mask, goggles and blue gloves, tinted blue"></div>
  <div class="abs partners">
    <div class="partner"><i style="background:var(--orange);border-radius:50%"></i>Harbour Health<br>Alliance</div>
    <div class="partner">Clearwater<br>Care Council</div>
    <div class="partner" style="color:var(--red);font-size:8px">Skillpath<br>Now</div>
    <div class="partner"><i style="background:var(--red)"></i></div>
    <div class="partner" style="color:#222;font-size:8px"><i style="background:var(--red)"></i>Westwork<br>Futures</div>
    <div class="partner" style="color:var(--navy)">Federal Learning<br>Office</div>
  </div>
  <div class="abs rule"></div>
  <div class="abs tagline">We're working for<br>Western Australia.</div>
  <div class="abs back-band">
    <div class="a">Carrow Academy of Learning<br>RTO 73648</div>
    <div class="b">FREECALL : 1800 437 982<br>info@carrowlearning.edu.au</div>
  </div>
  <div class="abs web">www.carrowlearning.edu.au</div>
</section>

<!-- Inside left -->
<section class="page p3">
  <div class="abs side-photo" role="img" aria-label="Photo of a smiling nurse in navy scrubs"></div>
  <div class="abs side-blue"></div>
  <div class="abs skills">
    <h4>Gain these skills :</h4>
    <ul>
      <li>Gain Industry Certification in Hand Hygiene</li>
      <li>Gain Industry Certification in COVID19 Infection Control</li>
      <li>Gain Industry Certification in Cleaning, Disinfection and Sterilisation</li>
      <li>Using personal protective equipment safely (practical session with complimentary PPE samples)</li>
      <li>Understanding the chain of infection</li>
      <li>Identify infection hazards and assess risks</li>
      <li>How to prevent the spread and transmission of infection<br>Maintaining a clean work environment</li>
    </ul>
  </div>
  <div class="abs ideal">
    <h4>Who this course is ideal for :</h4>
    <p>The skill set course is most suitable for anyone working the healthcare sector, or those looking to enter employment in the health fields.</p>
    <p><b>This training is for care workers across all health care settings, including:</b></p>
    <ul>
      <li>Hospitals</li>
      <li>Primary care</li>
      <li>Medical practices, allied health, GP and specialist clinics</li>
      <li>Aged care (both in residential aged care facilities or with visiting carers at home, including cleaners and cooks)</li>
    </ul>
  </div>
  <div class="abs col">
    <ul>
      <li>Disability (both in residential/shared care facilities or part-time carers in people's homes, including cleaners and cooks)</li>
      <li>Allied health</li>
      <li>Aboriginal Community Controlled Health Services</li>
      <li>Pharmacies</li>
      <li>Dental practices, including dentists, nurses, cleaners and receptionists</li>
    </ul>
    <h4>Job opportunities and<br>Study Pathways</h4>
    <p>This course does not lead to a specific job outcome but will be helpful if you are, or would like to work in any of the areas described above. Our training course is designed to make students Job Ready or to enhance their job role.</p>
    <p>The Units of Competency is a recognised Unit that can be used as a Credit Transfer in Qualifications such as :</p>
    <ul class="quals">
      <li>Certificate III Business Administration (Medical)</li>
      <li>Cert III and IV Health Administration</li>
      <li>Cert III in Individual Support (Aging, disability, home and community)</li>
      <li>Cert III in Allied Health Assistance</li>
      <li>Cert III/IV Dental Assisting</li>
      <li>Certificate III in Aboriginal and/or Torres Strait Islander Primary Health Care</li>
      <li>Cert II/III Community Services</li>
      <li>Certificate III in Cleaning Operations</li>
      <li>Cert II and III Health Support Services</li>
    </ul>
  </div>
  <div class="abs more"><b>More Qualifications</b> that include this Unit of Competency can be found at<small>https://unitregister.edu.au/details/HLTINF001</small></div>
  <div class="bars"><span class="o"></span><span class="r"></span><span class="b"></span></div>
</section>

<!-- Inside right -->
<section class="page p4">
  <div class="abs about-head">
    <h2>About this course</h2>
    <h5>Protect yourself and others in the community from infectious diseases</h5>
  </div>
  <div class="abs about-photo" role="img" aria-label="Photo of a nurse washing her hands at a clinic basin"></div>
  <div class="abs txt about-a">
    <p>There is not better time than now, to formally Upskill yourself and your team with a Nationally Accredited unit of Competency in Infection Control prevention including the latest COVID19 infection control protocols (Department of Health). Fast track your skills with Carrow's Accredited Infection Control Skill set to get you job ready or enhance your current workplace skills.</p>
    <p>The COVID19 pandemic has highlighted the important of building the capacity and understanding of the workforce to <span class="red">practice safe infection control procedures.</span></p>
    <p>This skill set will provide you with the skills and knowledge to assist in protecting yourself and others in the community from infectious diseases.</p>
  </div>
  <div class="abs txt about-b">
    <p>You will understand how infections are spread, ways of preventing the spread of infection and how to protect yourself and others from infection.</p>
    <p>The skill set is becoming increasingly important for all Health Care Workers – and all workers are encouraged to upskill themselves today, whether you are becoming Job Ready or for your professional development in Industry.</p>
  </div>
  <div class="abs format">
    <h3 class="first">Course format - Online with face-to-face tutorial (in person or via Meetwave)</h3>
    <div class="txt">
      <p>Our course is delivered to you online which allows you to undertake study at your own pace. It is recommended completion occurs within a month.</p>
      <p>you have completed the Online Component of your course, you are invited into a Practical Lab Session via face to face learning; to practice skills and undertake a workplace simulated activity.</p>
      <p>Regional locations may be fulfilled by Meetwave technology and Carrow may also conduct on-site visits as required. Carrow also travel to regional locations throughout the year. Group training sessions are also available for corporates and workplaces.</p>
    </div>
    <h3>Mentor Support and Practical Sessions</h3>
    <div class="txt"><p>Students are welcomed to the course by a short induction by your Tutor/Mentor to start you on your way with confidence! All of Carrow's student resources, learner materials, videos are contained in Carrow's easy to use LMS and learning is provided online at your convenience.</p></div>
    <h3>Industry Recognised</h3>
    <div class="txt"><p>Carrow's unique program in Infection Control is supported by leading Industry bodies, and includes certification by the Department of Health, and other leading Health bodies in Australia. Our Unit of competency is Australian Recognised and Accredited.</p></div>
  </div>
  <div class="bars"><span class="o"></span><span class="r"></span><span class="b"></span></div>
</section>

</body>
</html>
```